business card design

We are a company in Hong Kong, distribute & export aquariums and want a new business card. We have added our new fish tank in our new card but do want a better design.
Don't prefer fancy design as this is for export business and need to show overseas office contact.
But do want a professional design and a card that can tell we are in aquatic business.
I will attach a scan copy of current name card, the revised draft we just make, the content to show on name card and the logos
feel free to visit our webpage www.qv-reefhouse.com for more details.

```html
<!DOCTYPE html>
<html lang="en">
<head>
<meta charset="utf-8">
<title>Mira Chan – Business Card</title>
<link rel="stylesheet" href="https://fonts.googleapis.com/css2?family=Noto+Sans:wght@400;700&display=swap">
<style>
  :root {
    --aqua: #46c9bb;
    --band: #48cdc0;
    --paper: #ffffff;
    --tank-dark: #2e3134;
    --tank-mid: #6f7478;
    --water: #f4f6f7;
  }
  html, body {
    margin: 0;
    padding: 0;
    overflow: hidden;
    background: var(--paper);
  }
  .card {
    position: relative;
    width: 1200px;
    height: 741px;
    background: var(--paper);
    overflow: hidden;
    font-family: "Noto Sans", sans-serif;
    color: var(--aqua);
  }
  .product-visual {
    position: absolute;
    left: 74px;
    top: 150px;
    width: 434px;
    height: 420px;
    border-radius: 48% 48% 44% 44% / 50% 50% 46% 46%;
    background: radial-gradient(ellipse at 55% 50%, var(--water) 0%, var(--water) 52%, var(--tank-mid) 62%, var(--tank-dark) 72%);
  }
  .name {
    position: absolute;
    left: 614px;
    top: 168px;
    margin: 0;
    font-size: 72px;
    font-weight: 700;
    letter-spacing: 1px;
    line-height: 1;
  }
  .job-title {
    position: absolute;
    left: 710px;
    top: 252px;
    margin: 0;
    font-size: 26px;
    font-weight: 400;
    line-height: 1;
  }
  .contact-list {
    position: absolute;
    left: 610px;
    top: 0;
    margin: 0;
    font-size: 23px;
    line-height: 1;
  }
  .contact-row {
    position: absolute;
    left: 0;
    white-space: nowrap;
  }
  .contact-label { position: absolute; left: 0; }
  .contact-sep { position: absolute; left: 104px; }
  .contact-value { position: absolute; left: 142px; }
  .bottom-band {
    position: absolute;
    left: 0;
    top: 677px;
    width: 1200px;
    height: 64px;
    background: var(--band);
  }
</style>
</head>
<body>
  <div class="card">
    <div class="product-visual" role="img" aria-label="Round dark-framed fish tank with goldfish, aquatic plants and white pebbles"></div>

    <h1 class="name">Mira Chan</h1>
    <p class="job-title">Executive Assistant</p>

    <div class="contact-list">
      <div class="contact-row" style="top:345px">
        <span class="contact-label">Address</span><span class="contact-sep">:-</span>
        <span class="contact-value">7/F ., 48 Lok Shan Road,<br><span style="display:inline-block;margin-top:4px">Kowloon, Hong Kong</span></span>
      </div>
      <div class="contact-row" style="top:416px">
        <span class="contact-label">Phone</span><span class="contact-sep">:-</span>
        <span class="contact-value">(852)2461 0738</span>
      </div>
      <div class="contact-row" style="top:452px">
        <span class="contact-label">Fax</span><span class="contact-sep">:-</span>
        <span class="contact-value">(852) 2470 5912</span>
      </div>
      <div class="contact-row" style="top:498px">
        <span class="contact-label">Email</span><span class="contact-sep">:-</span>
        <span class="contact-value">Mira_chan @qvreef.com</span>
      </div>
      <div class="contact-row" style="top:532px">
        <span class="contact-label">Websit</span><span class="contact-sep">:-</span>
        <span class="contact-value" style="left:148px">www.qv-reefhouse.com</span>
      </div>
    </div>

    <div class="bottom-band"></div>
  </div>
</body>
</html>
```